Design a modern, classy & professional business card for an online real estate agency, specializing in medium-luxury properties in Thailand and later in Singapore and UK.

Possible design ideas so far: (not essential)

- curved corner(s) to the card, white on front & turquoise on back or visa versa.

- front of card - clear and simple, company name in metallic grey/monochrome, logo graphic & company name on front in spot UV or embossed/debossed effect.

- back of card - large, close-cropped, 'ghost' patterns of the C-shaped curves of logo, or company name repeated on back of card in spot UV.

Target Market(s)

- young to middle-aged professionals mainly (but ideally should design should suit all)

- UK, US,EU,AUS & ASIAN mainly (but ideally should design should suit all countries)

Industry/Entity Type

Real Estate

Requirements
Must have
• THEME:
- Luxurious & Modern
- Clean & striking
- Unique & creative

INFO:
- Logo & company name on front
- Contact details on back:

Tobias Lindqvar
Managing Director

www.velmoraestates.example
www.velmoraestates-uk.example

Tel: 084-273-6190
email: tobias@velmoraestates.example

(contact details can be displayed in any order as suites design.)

Nice to have
• - curved corner(s) to the card, white on front & turquoise on back or visa versa.

Should not have
• - No generic images of properties, palm trees/coconut trees etc.

- No other other bold colors, except for main turquoise, grey, metallic white & black theme.

- No obvious business card templates

```html
<!DOCTYPE html>
<html lang="en">
<head>
<meta charset="utf-8">
<title>Velmora Estates – Business Card</title>
<link rel="stylesheet" href="https://fonts.googleapis.com/css2?family=Montserrat:ital,wght@0,400;0,500;0,700;1,400&display=swap">
<style>
  :root {
    --stage: #e4e5e6;
    --card: #ffffff;
    --texture-light: #fbfbfb;
    --texture-dark: #f0f0f0;
    --teal: #6bbfbc;
    --teal-deep: #5aaeab;
    --grey: #6b6b6b;
    --charcoal: #55575a;
    --ink: #333333;
  }
  * { box-sizing: border-box; margin: 0; padding: 0; }
  html, body {
    width: 1200px;
    height: 675px;
    overflow: hidden;
    background: var(--stage);
    font-family: "Montserrat", Arial, sans-serif;
  }
  .stage {
    position: relative;
    width: 1200px;
    height: 675px;
  }
  .card {
    position: absolute;
    top: 187px;
    width: 525px;
    height: 300px;
    background: var(--card);
    overflow: hidden;
    box-shadow: 0 2px 6px rgba(0,0,0,0.12);
  }
  .card--front { left: 50px; }
  .card--back { left: 625px; }

  .card__texture {
    position: absolute;
    inset: 0;
    background: radial-gradient(ellipse at 40% 40%, var(--texture-light) 0%, var(--texture-dark) 100%);
  }

  .brand {
    position: absolute;
    display: flex;
    align-items: center;
  }
  .brand__square {
    background: var(--teal);
    flex: none;
  }
  .brand__name {
    font-weight: 500;
    color: var(--grey);
    white-space: nowrap;
  }
  .card--front .brand { left: 88px; top: 110px; gap: 20px; }
  .card--front .brand__square { width: 76px; height: 76px; }
  .card--front .brand__name { font-size: 38px; letter-spacing: 0.5px; }

  .card--back .brand { left: 40px; top: 40px; gap: 14px; }
  .card--back .brand__square { width: 54px; height: 54px; }
  .card--back .brand__name { font-size: 27px; letter-spacing: 0.3px; }

  .person {
    position: absolute;
    left: 150px;
    top: 200px;
    text-align: right;
  }
  .person__name {
    font-weight: 700;
    font-size: 16px;
    color: var(--teal);
  }
  .person__role {
    font-style: italic;
    font-size: 12px;
    color: var(--charcoal);
    margin-top: 3px;
  }

  .contacts {
    position: absolute;
    left: 300px;
    top: 108px;
    list-style: none;
  }
  .contacts__item {
    display: flex;
    align-items: center;
    gap: 8px;
    font-size: 11.5px;
    color: var(--ink);
    height: 19px;
  }
  .contacts__icon { width: 13px; height: 13px; flex: none; }
  .contacts__accent { color: var(--teal); }

  .card__bands {
    position: absolute;
    left: 0;
    bottom: 0;
    width: 525px;
    height: 120px;
  }
</style>
</head>
<body>
<main class="stage">

  <section class="card card--front" aria-label="Card front">
    <div class="card__texture" role="img" aria-label="Faint ghost pattern of interlocking rings across the card"></div>
    <div class="brand">
      <span class="brand__square"></span>
      <span class="brand__name">Velmora Estates</span>
    </div>
  </section>

  <section class="card card--back" aria-label="Card back">
    <div class="card__texture" role="img" aria-label="Faint ghost pattern of interlocking rings across the card"></div>

    <svg class="card__bands" viewBox="0 0 525 120" aria-hidden="true">
      <polygon points="330,62 525,20 525,34 380,62" fill="var(--charcoal)"/>
      <polygon points="0,112 525,54 525,120 0,120" fill="var(--teal)"/>
      <polygon points="0,116 525,60 525,120 0,120" fill="var(--card)" opacity="0.0"/>
    </svg>

    <div class="brand">
      <span class="brand__square"></span>
      <span class="brand__name">Velmora Estates</span>
    </div>

    <ul class="contacts">
      <li class="contacts__item">
        <svg class="contacts__icon" viewBox="0 0 16 16" aria-hidden="true"><path d="M3 2h3l1 3-2 1.5a9 9 0 0 0 4.5 4.5L11 9l3 1v3a1 1 0 0 1-1 1A12 12 0 0 1 2 3a1 1 0 0 1 1-1z" fill="var(--charcoal)"/></svg>
        <span>084-273-6190</span>
      </li>
      <li class="contacts__item">
        <svg class="contacts__icon" viewBox="0 0 16 16" aria-hidden="true"><rect x="1" y="3" width="14" height="10" fill="var(--charcoal)"/><path d="M1 3l7 6 7-6" fill="none" stroke="#fff" stroke-width="1.2"/></svg>
        <span>tobias@<span class="contacts__accent">velmoraestates</span>.example</span>
      </li>
      <li class="contacts__item">
        <svg class="contacts__icon" viewBox="0 0 16 16" aria-hidden="true"><circle cx="8" cy="8" r="7" fill="var(--charcoal)"/><path d="M1 8h14M8 1c-3 3.5-3 10.5 0 14M8 1c3 3.5 3 10.5 0 14" fill="none" stroke="#fff" stroke-width="0.9"/></svg>
        <span>www.<span class="contacts__accent">velmoraestates</span>.example</span>
      </li>
      <li class="contacts__item">
        <svg class="contacts__icon" viewBox="0 0 16 16" aria-hidden="true"><circle cx="8" cy="8" r="7" fill="var(--charcoal)"/><path d="M1 8h14M8 1c-3 3.5-3 10.5 0 14M8 1c3 3.5 3 10.5 0 14" fill="none" stroke="#fff" stroke-width="0.9"/></svg>
        <span>www.<span class="contacts__accent">velmoraestates-uk</span>.example</span>
      </li>
    </ul>

    <div class="person">
      <p class="person__name">Tobias Lindqvar</p>
      <p class="person__role">Managing Director</p>
    </div>
  </section>

</main>
</body>
</html>
```